A professional business to business web site for a contract agency called VONTAREX.

We need a very clean, very professional web site created for business to business. It is an informational web site with 3 pages. We are a company that offers contract employee placements into primarily the pharmaceutical industry. I have attached a file that describes the company more fully.

Hi,

I'm sorry if I wasn't clear, but I need to have the HTML pages created so I can just upload the files you give me to the web hosting site.

Please let me know if you have any questions.

Thanks for working on my project!

Hello,

I didn't put this in the description, but I would need the web site set up on the web hosting site as well.  The web hosting site is abrightkettle.  I want a copy of all the files as well.

Thanks,
Miles

Reason: I'm sorry, unexpectedly, I have been very busy and I haven't been able to devote the time necessary for this. I am extending the deadline by 10 days. Thank you for your patience. Thanks.

Reason: Hi everyone, I apologize again, but everything has been so busy here that I haven't been able to give this attention. I plan to work on this over the next few days. Thanks and sorry again, Miles.

Reason: I'm sorry this is taking longer than planned. I have been extremely busy. I have increased the budget on this project. Thanks.

Target Market(s)

Large professional corporations mainly in the pharmaceutical industry. The audience is hiring decisions makers within the companies and potential job candidates/job seekers.

Industry/Entity Type

Pharmaceutical

Font styles to use
Sans Serif

Requirements
Must have
• Must have a clean look that mimics the pharmaceutical industry web sites. VERY professional.
Nice to have
• A nice picture of professional business/pharma/technical people looking like a team. Colors are listed on the attached Word document.
Should not have
• No animation. Not too busy.

```html
<!DOCTYPE html>
<html lang="en">
<head>
<meta charset="utf-8">
<title>VONTAREX – Enhancing your team</title>
<link href="https://fonts.googleapis.com/css2?family=Figtree:wght@300;400;600;700&display=swap" rel="stylesheet">
<style>
:root{
  --blue:#1b5a85;
  --blue-dark:#13476b;
  --blue-light:#2a79a8;
  --orange:#ff8a00;
  --orange-dark:#e06f00;
  --ink:#2b2b2b;
  --muted:#9a9a9a;
  --line:#e4e4e4;
  --card:#f4f4f4;
  --white:#ffffff;
}
*{box-sizing:border-box;margin:0;padding:0}
html,body{width:744px;height:1200px;overflow:hidden;background:var(--white)}
body{font-family:"Figtree",Arial,sans-serif;color:var(--ink)}
.page{position:relative;width:900px;height:1452px;transform:scale(0.82667);transform-origin:0 0}
.abs{position:absolute}

/* header */
.site-header{position:absolute;left:0;top:0;width:900px;height:70px;border-bottom:1px solid var(--line)}
.brand{position:absolute;left:161px;top:16px;display:flex;align-items:center;gap:10px}
.brand-mark{width:40px;height:36px;border-radius:50%;background:var(--blue)}
.brand-name{font-size:19px;font-weight:600;letter-spacing:4px;color:var(--blue);line-height:1}
.brand-tag{font-size:11.5px;color:var(--ink);margin-top:3px}
.top-contact{position:absolute;top:8px;right:177px;font-size:9px;display:flex;gap:20px;color:#777}
.top-contact .mail{color:var(--blue)}
.top-contact svg{vertical-align:-1px;margin-right:3px}
.main-nav{position:absolute;top:30px;left:527px;display:flex;align-items:center;font-size:12px}
.main-nav a{text-decoration:none;color:var(--ink)}
.nav-home{background:var(--blue);color:var(--white)!important;font-weight:600;width:68px;height:26px;display:flex;align-items:center;justify-content:center;border-bottom:3px solid #6c9ab8}
.main-nav .nav-services{margin-left:16px}
.main-nav .nav-contact{margin-left:24px}

/* hero */
.hero-title{left:161px;top:120px;font-size:24px;font-weight:300;line-height:30px;color:#333;z-index:2;white-space:nowrap}
.hero-text{left:161px;top:196px;width:285px;font-size:13.2px;line-height:18px;z-index:2}
.btn-orange{background:var(--orange);color:var(--white);font-weight:600;display:flex;align-items:center;justify-content:center;border-bottom:3px solid var(--orange-dark)}
.quote-btn{left:160px;top:273px;width:171px;height:37px;font-size:17px}
.hero-photo{left:486px;top:80px;width:284px;height:223px;z-index:1;background:linear-gradient(90deg,#d8c3a8 0%,#8a8a8a 40%,#5a5a5a 70%,#f2f2f2 100%)}

/* partners */
.partners{left:0;top:365px;width:900px;height:98px;border-top:2px solid var(--line);display:flex;align-items:center}
.partners-label{margin-left:161px;font-size:13px;color:var(--muted);width:100px}
.partner{font-size:22px;color:#9d9d9d;margin-right:60px;display:flex;align-items:center;gap:8px}
.partner i{display:inline-block;width:16px;height:16px;background:#b5b5b5}

/* services */
.services{left:0;top:463px;width:900px;height:401px;background:radial-gradient(ellipse at 50% 45%,#2b77a4 0%,var(--blue) 60%,#175079 100%)}
.tab{position:absolute;top:34px;height:44px;font-size:18px;display:flex;align-items:center;justify-content:center}
.tab-clients{left:252px;width:190px;background:var(--white);color:var(--blue);border-bottom:3px solid #c3c3c3}
.tab-seeking{left:466px;width:190px;background:#2172a8;color:var(--white);border-bottom:3px solid #4b8fbf}
.service{position:absolute;top:120px;width:190px;text-align:center;color:var(--white)}
.service svg{display:block;margin:0 auto;height:70px}
.service h3{font-weight:400;font-size:18.5px;line-height:23px;margin-top:24px}
.service p{font-size:11.4px;line-height:14.6px;margin-top:17px}
.service .btn-orange{width:99px;height:30px;font-size:13px;margin:18px auto 0}

/* news */
.section-label{font-size:13.5px;color:var(--muted)}
.news-card{position:absolute;top:927px;width:180px;height:269px;background:var(--card);border-bottom:3px solid #dedede}
.news-photo{height:123px;border-bottom:2px solid #c07a4a}
.news-card h4{font-weight:400;font-size:13.5px;line-height:18px;color:#333;margin:9px 11px 0;padding-bottom:7px;border-bottom:1px solid #dcdcdc}
.news-card p{font-size:10.5px;line-height:14px;margin:8px 11px 0}
.read-more{position:absolute;left:11px;bottom:10px;width:87px;height:23px;background:var(--blue);color:var(--white);font-size:11.5px;font-weight:600;display:flex;align-items:center;justify-content:center;border-bottom:2px solid #6c9ab8}

/* contact */
.map{left:161px;top:1261px;width:180px;height:114px;background:linear-gradient(135deg,#ebe6dc,#f3efe6 50%,#e8d9a8);border-bottom:3px solid #d6d6d6}
.contact-list{left:358px;top:1278px;list-style:none;font-size:14px;color:#333}
.contact-list li{display:flex;align-items:center;height:28.5px}
.contact-list svg{width:14px;margin-right:8px;fill:#333}

/* footer */
.site-footer{left:0;top:1394px;width:900px;height:58px;background:var(--blue);color:var(--white);font-size:12px;font-weight:600}
.site-footer .copy{position:absolute;left:162px;top:17px}
.footer-links{position:absolute;left:543px;top:17px;display:flex;gap:20px}
.footer-links span::before{content:"";display:inline-block;width:5px;height:5px;border-radius:50%;background:var(--white);margin-right:12px;vertical-align:2px}
</style>
</head>
<body>
<div class="page">

  <header class="site-header">
    <div class="brand">
      <span class="brand-mark"></span>
      <div>
        <div class="brand-name">VONTAREX</div>
        <div class="brand-tag">Enhancing your team</div>
      </div>
    </div>
    <div class="top-contact">
      <span><svg width="8" height="8" viewBox="0 0 24 24"><path fill="#777" d="M6.6 10.8a15 15 0 006.6 6.6l2.2-2.2c.3-.3.7-.4 1-.2 1.1.4 2.3.6 3.6.6.6 0 1 .4 1 1V20c0 .6-.4 1-1 1A17 17 0 013 4c0-.6.4-1 1-1h3.5c.6 0 1 .4 1 1 0 1.3.2 2.5.6 3.6.1.3 0 .7-.2 1z"/></svg>555-014-2290</span>
      <span class="mail"><svg width="9" height="7" viewBox="0 0 24 18"><path fill="#1b5a85" d="M0 0h24v2L12 10 0 2zM0 4l12 8 12-8v14H0z"/></svg>contact.us@VONTAREX.com</span>
    </div>
    <nav class="main-nav">
      <a class="nav-home" href="#">Home</a>
      <a class="nav-services" href="#">Services</a>
      <a class="nav-contact" href="#">Contact</a>
    </nav>
  </header>

  <div class="abs hero-photo" role="img" aria-label="Photo of a confident businesswoman in front of a team of professionals"></div>
  <h1 class="abs hero-title">We look for the top people<br>and companies to work with.</h1>
  <p class="abs hero-text">Whether you are looking for a position, or looking for a contractor, you have come to the right place.</p>
  <div class="abs btn-orange quote-btn">Reqest a Quote</div>

  <div class="abs partners">
    <span class="partners-label">As seen in:</span>
    <span class="partner"><i></i>Veranthe</span>
    <span class="partner"><i></i>Corvexa</span>
    <span class="partner"><i></i>Lumidra</span>
  </div>

  <section class="abs services">
    <div class="tab tab-clients">Client Companies</div>
    <div class="tab tab-seeking">Seeking Positions</div>

    <div class="service" style="left:156px">
      <svg viewBox="0 0 70 66" width="70"><path fill="#fff" d="M16 2h50l-10 52H6z"/><path fill="#1b5a85" d="M24 10h32l-1.5 7h-32zM22 22h32l-1.5 7h-32z"/><path fill="none" stroke="#fff" stroke-width="5" d="M6 54c-4 6 0 9 5 9h46"/></svg>
      <h3>Project<br>Management</h3>
      <p>VONTAREX offers professional project managers that can work remotely or onsite.</p>
      <div class="btn-orange">More</div>
    </div>

    <div class="service" style="left:348px">
      <svg viewBox="0 0 60 66" width="60"><circle cx="30" cy="15" r="14" fill="#fff"/><path fill="#fff" d="M2 66V48c0-10 8-16 16-16h24c8 0 16 6 16 16v18z"/><circle cx="16" cy="52" r="5" fill="none" stroke="#1b5a85" stroke-width="3"/><circle cx="44" cy="52" r="5" fill="none" stroke="#1b5a85" stroke-width="3"/><path fill="none" stroke="#1b5a85" stroke-width="3" d="M16 47v-7c0-5 4-8 14-8M44 47v-7c0-5-4-8-14-8"/></svg>
      <h3>Chromatography<br>instrument</h3>
      <p>VONTAREX offers Kestral Informatics software training through contract employees.</p>
      <div class="btn-orange">More</div>
    </div>

    <div class="service" style="left:542px">
      <svg viewBox="0 0 62 66" width="62"><path fill="none" stroke="#fff" stroke-width="5" stroke-linejoin="round" d="M20 3h22M24 3v20L4 61h54L38 23V3"/><path fill="#fff" d="M14 44h34l8 16H6z"/></svg>
      <h3>Laboratory<br>positions</h3>
      <p>VONTAREX has a vast network of laboratory and laboratory con-tacts to find your next...</p>
      <div class="btn-orange">More</div>
    </div>
  </section>

  <div class="abs section-label" style="left:161px;top:895px">Latest News:</div>

  <article class="news-card" style="left:161px">
    <div class="news-photo" role="img" aria-label="Photo of medical staff in blue scrubs" style="background:linear-gradient(90deg,#3a5f86,#8fb3cf 50%,#dfe6ee)"></div>
    <h4>Our Network of<br>Doctors</h4>
    <p>Lorem Ipsum, you need to be sure there isn't anything em-barrassing</p>
    <span class="read-more">Read more</span>
  </article>
  <article class="news-card" style="left:355px">
    <div class="news-photo" role="img" aria-label="Photo of a doctor with a stethoscope in a consultation" style="background:linear-gradient(90deg,#e8e8e8,#8a7160 45%,#5a4a42 75%,#bcbcbc)"></div>
    <h4>Encouraging<br>Professionals</h4>
    <p>Lorem Ipsum, you need to be sure there isn't anything em-barrassing</p>
    <span class="read-more">Read more</span>
  </article>
  <article class="news-card" style="left:553px">
    <div class="news-photo" role="img" aria-label="Photo of a team of doctors in a hospital corridor" style="background:linear-gradient(90deg,#2aa3c4,#6b8fa7 40%,#3f5e78 70%,#21b3d0)"></div>
    <h4>Our Network of<br>Doctors</h4>
    <p>Lorem Ipsum, you need to be sure there isn't anything em-barrassing</p>
    <span class="read-more">Read more</span>
  </article>

  <div class="abs section-label" style="left:161px;top:1228px">Get in Touch with us</div>
  <div class="abs map" role="img" aria-label="Street map showing the office location"></div>
  <ul class="abs contact-list">
    <li><svg viewBox="0 0 24 24"><path d="M6.6 10.8a15 15 0 006.6 6.6l2.2-2.2c.3-.3.7-.4 1-.2 1.1.4 2.3.6 3.6.6.6 0 1 .4 1 1V20c0 .6-.4 1-1 1A17 17 0 013 4c0-.6.4-1 1-1h3.5c.6 0 1 .4 1 1 0 1.3.2 2.5.6 3.6.1.3 0 .7-.2 1z"/></svg>555-014-2290</li>
    <li><svg viewBox="0 0 24 24"><path d="M12 1a8 8 0 00-8 8c0 6 8 14 8 14s8-8 8-14a8 8 0 00-8-8zm0 11a3 3 0 110-6 3 3 0 010 6z"/></svg>1820 Harbor Crest Lane, Bayview, CA&nbsp; 90210</li>
    <li><svg viewBox="0 0 24 18"><path d="M0 0h24v2L12 10 0 2zM0 4l12 8 12-8v14H0z"/></svg>contact.us@VONTAREX.com</li>
  </ul>

  <footer class="abs site-footer">
    <span class="copy">Vontarex - Enhancing your team 2014 Copyright!</span>
    <div class="footer-links"><span>Privacy Policy</span><span>Terms of Use</span></div>
  </footer>

</div>
</body>
</html>
```